Postcard Design

We are a full service lawn and landscape maintenance business. Employees are myself as owner-operator and
my son as operator and pesticide applicator and hardscape designer and builder along with myself as helper in the
hardscape. We have over 30 years experience and have operated as Dale's Yard Cutting for 23 years since 1993.
We are dependable and reasonably priced and hard working. My son is an excellent operator. We are full service year round. Spring cleanups, Summer all service, Fall cleanups and Winter snow removal.

Industry/Entity Type

Business

```html
<!DOCTYPE html>
<html lang="en">
<head>
<meta charset="utf-8">
<title>Dale's Yard Cutting – Postcard</title>
<link rel="stylesheet" href="https://fonts.googleapis.com/css2?family=Arimo:wght@700&family=Jost:wght@400;500;600&family=Oswald:wght@300;400&display=swap">
<style>
  :root {
    --backdrop: #2a2a2a;
    --grass-dark: #3f6f1c;
    --grass-mid: #6f9a34;
    --grass-light: #9fbf5a;
    --lawn-back: #7aa58a;
    --lawn-back-light: #a8c8b0;
    --teal: #2cc5c0;
    --teal-band: rgba(36, 196, 190, 0.82);
    --cyan: #12c8ee;
    --leaf: #39c43a;
    --banner: #1a8fd0;
    --fold: #2b2b2b;
    --ink: #2a3a30;
    --white: #ffffff;
    --glow: #2fb82b;
  }
  * { box-sizing: border-box; margin: 0; padding: 0; }
  html, body { width: 900px; height: 1200px; overflow: hidden; }
  body { background: var(--backdrop); position: relative; font-family: "Jost", sans-serif; }

  .card { position: absolute; left: 62px; width: 776px; height: 502px; overflow: hidden; }
  .card--front { top: 60px; }
  .card--back { top: 638px; background: var(--white); }

  /* front */
  .front-photo {
    position: absolute; inset: 0;
    background:
      radial-gradient(ellipse 320px 260px at 600px 230px, rgba(40,40,40,0.55), transparent 70%),
      radial-gradient(ellipse 180px 140px at 650px 240px, rgba(200,40,40,0.45), transparent 70%),
      linear-gradient(180deg, var(--grass-light) 0%, var(--grass-mid) 35%, var(--grass-dark) 100%);
  }
  .brand {
    position: absolute; left: 52px; top: 48px;
    font-family: "Arimo", sans-serif; font-weight: 700; color: var(--white);
    line-height: 1.22; text-transform: uppercase;
    text-shadow: 0 0 3px var(--glow), 0 0 3px var(--glow), 0 0 6px var(--glow);
  }
  .brand__name { display: block; font-size: 40px; }
  .brand__line { display: block; font-size: 37px; }
  .tagline {
    position: absolute; left: 53px; top: 222px;
    color: var(--white); font-size: 27px; line-height: 36px; font-weight: 400;
  }
  .season-band {
    position: absolute; left: 0; top: 365px; width: 565px; height: 36px;
    background: var(--teal-band);
    clip-path: polygon(0 0, 100% 0, 96% 100%, 0 100%);
    color: var(--white); font-weight: 600; font-size: 20px;
    padding: 6px 0 0 52px;
  }
  .services { position: absolute; left: 52px; top: 406px; list-style: none; color: var(--white); font-size: 20px; line-height: 27px; }
  .services li { display: flex; align-items: center; gap: 6px; }
  .services svg { width: 15px; height: 15px; }
  .call-band {
    position: absolute; left: 556px; top: 392px; width: 220px; height: 40px;
    background: var(--teal-band);
    clip-path: polygon(4% 0, 100% 0, 100% 100%, 0 100%);
    color: var(--white); font-family: "Oswald", sans-serif; font-size: 27px; font-weight: 400;
    text-align: right; padding: 0 8px 0 0; line-height: 40px;
  }
  .phone {
    position: absolute; left: 564px; top: 444px; display: flex; align-items: center; gap: 10px;
    color: var(--white); font-family: "Oswald", sans-serif; font-weight: 300; font-size: 28px;
  }
  .phone svg { width: 34px; height: 34px; }

  /* back */
  .back-art { position: absolute; inset: 0; }
  .story { position: absolute; left: 37px; top: 36px; width: 420px; color: var(--ink); }
  .story__lead { font-size: 15px; font-weight: 500; text-transform: uppercase; line-height: 20px; }
  .story__p { font-size: 17.5px; line-height: 22px; }
  .story__big { font-size: 20px; line-height: 28px; }
  .story__bold { font-size: 21px; line-height: 28px; font-weight: 500; margin-top: 8px; }
  .story__close { font-size: 17px; line-height: 24px; font-weight: 500; margin-top: 10px; }
  .contact-title {
    position: absolute; left: 0; top: 368px; width: 489px; height: 100px;
    background: var(--banner); color: var(--white);
    font-size: 36px; font-weight: 400; line-height: 100px; padding-left: 78px;
  }
  .stamp-box { position: absolute; left: 666px; top: 27px; width: 84px; height: 96px; border: 1px solid #555; }
  .address-line { position: absolute; left: 530px; width: 220px; height: 1px; background: #333; }
</style>
</head>
<body>

<section class="card card--front">
  <div class="front-photo" role="img" aria-label="Photo of a red and black lawn mower on a green lawn"></div>
  <h1 class="brand">
    <span class="brand__name">Dale's</span>
    <span class="brand__line">Yard Cutting</span>
    <span class="brand__line">Services</span>
  </h1>
  <p class="tagline">We Are A Full Service<br>Lawn And Landscape<br>Maintenance</p>
  <div class="season-band">We Are Full Service Year Round.</div>
  <ul class="services">
    <li><svg viewBox="0 0 16 16"><circle cx="8" cy="8" r="6.5" fill="none" stroke="#2cc5c0" stroke-width="1.5"/><path d="M4.8 8.2l2.2 2.2 4.2-4.4" fill="none" stroke="#2cc5c0" stroke-width="1.6"/></svg>Spring Cleanups</li>
    <li><svg viewBox="0 0 16 16"><circle cx="8" cy="8" r="6.5" fill="none" stroke="#2cc5c0" stroke-width="1.5"/><path d="M4.8 8.2l2.2 2.2 4.2-4.4" fill="none" stroke="#2cc5c0" stroke-width="1.6"/></svg>Summer All Service</li>
    <li><svg viewBox="0 0 16 16"><circle cx="8" cy="8" r="6.5" fill="none" stroke="#2cc5c0" stroke-width="1.5"/><path d="M4.8 8.2l2.2 2.2 4.2-4.4" fill="none" stroke="#2cc5c0" stroke-width="1.6"/></svg>Fall Cleanups And Winter Snow Removal</li>
  </ul>
  <div class="call-band">CALL US NOW</div>
  <div class="phone">
    <svg viewBox="0 0 34 34"><circle cx="17" cy="17" r="15" fill="none" stroke="#2cc5c0" stroke-width="2.5"/><path d="M11.5 9.5l3 0 1.5 4-2 1.5c1 2.2 2.8 4 5 5l1.5-2 4 1.5 0 3c0 1-1 2-2 2-7 0-13-6-13-13 0-1 1-2 2-2z" fill="#2cc5c0"/></svg>
    (123) 4567 890
  </div>
</section>

<section class="card card--back">
  <svg class="back-art" viewBox="0 0 776 502" width="776" height="502">
    <defs>
      <linearGradient id="lawn" x1="0" y1="0" x2="0" y2="1">
        <stop offset="0" stop-color="#a8c8b0"/>
        <stop offset="1" stop-color="#6f9f78"/>
      </linearGradient>
      <clipPath id="lawn-clip"><circle cx="18" cy="252" r="455"/></clipPath>
    </defs>
    <circle cx="18" cy="252" r="478" fill="#12c8ee"/>
    <circle cx="18" cy="252" r="466" fill="#39c43a"/>
    <rect width="776" height="502" fill="url(#lawn)" clip-path="url(#lawn-clip)" role="img" aria-label="Photo of a freshly striped green lawn"/>
    <polygon points="390,468 489,468 489,490 452,502 380,502" fill="#2b2b2b"/>
  </svg>
  <div class="story">
    <p class="story__lead">My son as operator and pesticide<br>applicator and hardscape designer</p>
    <p class="story__p" style="margin-top:4px">And Builder Along With Myself As Helper<br>In The Hardscape.</p>
    <p class="story__big">We Have Over 30 Years Experience</p>
    <p class="story__bold">And Have Operated As<br>Dale's Yard Cutting<br>For 23 Years Since 1993.</p>
    <p class="story__close">We Are Dependable And Reasonably Priced<br>And Hard Working. My Son Is An<br>Excellent Operator.</p>
  </div>
  <h2 class="contact-title">Contact Information</h2>
  <div class="stamp-box"></div>
  <div class="address-line" style="top:292px"></div>
  <div class="address-line" style="top:328px"></div>
  <div class="address-line" style="top:364px"></div>
</section>

</body>
</html>
```